Property investment company needs a letterhead design!

We are a new residential and commercial property investment company. Name of the company is Morvesta Group, LLC. We have a new logo and now we need letterhead! We prefer to have a professional and upscale appearance. We don't have any fixed requirements, so be creative! Thank you for considering this project. We are so excited to see what happens!

Target Market(s)

Professional

Industry/Entity Type

Real Estate Development

```html
<!DOCTYPE html>
<html lang="en">
<head>
<meta charset="utf-8">
<title>Morvesta Group, LLC — Letterhead</title>
<link href="https://fonts.googleapis.com/css2?family=Source+Sans+3:wght@400;800&display=swap" rel="stylesheet">
<style>
  :root {
    --backdrop: #e9e6e3;
    --paper: #ffffff;
    --paper-shade: #f2f2f2;
    --brand-green: #8cc63f;
    --brand-green-light: #a6d45f;
    --brand-navy: #0c1f3d;
    --ink: #1a1a1a;
  }
  * { box-sizing: border-box; margin: 0; padding: 0; }
  html, body {
    width: 927px;
    height: 1200px;
    overflow: hidden;
    background: var(--backdrop);
  }
  .letterhead {
    position: relative;
    width: 774px;
    height: 1200px;
    margin: 0 auto;
    background: linear-gradient(90deg, var(--paper-shade), var(--paper) 30%, var(--paper));
    overflow: hidden;
    font-family: "Source Sans 3", "Helvetica Neue", Arial, sans-serif;
    color: var(--ink);
  }
  .letterhead__top-band {
    position: absolute;
    left: 0;
    top: 0;
    width: 100%;
    height: 190px;
    background: linear-gradient(180deg, var(--brand-green) 0%, var(--brand-green) 60%, var(--brand-green-light) 100%);
  }
  .letterhead__bottom-band {
    position: absolute;
    left: 0;
    bottom: 0;
    width: 100%;
    height: 200px;
    background: linear-gradient(180deg, var(--brand-green) 0%, var(--brand-navy) 22%, var(--brand-navy) 100%);
  }
  .brand {
    position: absolute;
    left: 30px;
    top: 52px;
    display: flex;
    align-items: center;
    gap: 12px;
  }
  .brand__dot {
    width: 44px;
    height: 44px;
    border-radius: 50%;
    background: var(--brand-navy);
  }
  .brand__name {
    font-weight: 800;
    font-size: 26px;
    line-height: 1.05;
    color: var(--brand-navy);
    letter-spacing: 0.02em;
  }
  .letter {
    position: absolute;
    left: 50px;
    top: 268px;
    width: 700px;
    font-size: 19px;
    line-height: 25px;
  }
  .letter p + p { margin-top: 25px; }
  .letter p.tight { margin-top: 0; }
</style>
</head>
<body>
  <main class="letterhead">
    <div class="letterhead__top-band" role="img" aria-label="Green header band with flowing swoosh decoration"></div>
    <div class="letterhead__bottom-band" role="img" aria-label="Navy footer band with green wave decoration"></div>

    <header class="brand">
      <span class="brand__dot"></span>
      <span class="brand__name">Morvesta<br>Group, LLC</span>
    </header>

    <section class="letter">
      <p>Name<br>Title<br>Company<br>Address<br>City, State Zip Code</p>
      <p>Greeting (Salutation Examples)</p>
      <p>Dear Mr./Ms. Last Name:<br>
        Use a formal salutation, not a first name, unless you know the person well. If you do not know the person's gender, you can write out their full name. For instance, "Dear Lee Danvers" instead of "Dear Mr. Danvers" or "Dear Ms. Danvers." If you do not know the recipient's name, it's still common and acceptable to use the old-fashioned "To Whom It May Concern."</p>
      <p>Body of Letter</p>
      <p>The first paragraph of your letter should provide an introduction as to why you are writing so that your reason for contacting the person is obvious from the beginning. Then, in the following paragraphs, provide specific details about your request or information you are providing.</p>
      <p class="tight">The last paragraph of your letter should reiterate the reason you are writing and thank the reader for reviewing your request. If appropriate, it should also politely ask for a written response or for the opportunity to arrange a meeting to further discuss.<br>Closing</p>
      <p>Best regards, (Closing Examples)</p>
    </section>
  </main>
</body>
</html>
```